Business card for a Exhibition booth fabrication company

Hi. My company would like to change our corporate name card. We are an events and Exhibition stand builder company. We would like our corporate name card to resonate what we do. I need someone to create something unique that relates to the industry that I am in. The graphic designer should be creative to incorporate the elements of my industry and try to blend in well in the design of the card. Our aim is to ensure that we are unique and our card can look different from our competitors.
Updates

The decision maker was very busy and didnt had time to make this decision

Target Market(s)

Marketing and events manager from all companies

Contact Information for Business Card

The business card should have the following details:
Name
Job Title
Email
Website

Colors

Designer to choose colors to be used in the design.

Requirements
Must have
• The card must be look something that is relevant to the service that I am providing. My website is: www.velmora-buildworks.example
• You can see my website to get more information on what service that I am doing
Nice to have
• On the back of my card, I would like to have a globe image with the incorporation of my company logo. This is to indicate that my services can be done in any part of the world.

```html
<!DOCTYPE html>
<html lang="en">
<head>
<meta charset="utf-8">
<title>Velmora Buildworks – Business Card</title>
<link href="https://fonts.googleapis.com/css2?family=Lato:wght@400;700&family=Libre+Baskerville:wght@700&family=Montserrat:wght@500&display=swap" rel="stylesheet">
<style>
  :root {
    --red: #ed1c24;
    --red-dark: #b31119;
    --charcoal: #303030;
    --ink: #2b2b2b;
    --grey: #555555;
    --paper: #ffffff;
    --service-red: #b5121b;
  }
  * { margin: 0; padding: 0; box-sizing: border-box; }
  html, body { width: 1200px; height: 1200px; overflow: hidden; background: var(--paper); }
  .sheet { position: relative; width: 1200px; height: 1200px; }

  .card-frame {
    position: absolute; left: 304px; width: 635px; height: 363px;
    overflow: hidden; outline: 1px solid var(--ink); background: var(--paper);
  }
  .card-frame.front { top: 181px; }
  .card-frame.back { top: 617px; }
  .card {
    position: absolute; left: 0; top: 0; width: 1015px; height: 580px;
    transform: scale(0.6256); transform-origin: 0 0;
  }
  .card-shapes { position: absolute; inset: 0; width: 1015px; height: 580px; }

  .brand {
    position: absolute; display: flex; align-items: center; gap: 14px;
    font-family: "Montserrat", sans-serif; font-weight: 500;
    letter-spacing: 3px; color: var(--grey); font-size: 20px; white-space: nowrap;
  }
  .brand-dot { width: 22px; height: 22px; border-radius: 50%; background: var(--red); flex: none; }
  .front .brand { left: 88px; top: 130px; }
  .back .brand { left: 0; right: 0; top: 185px; justify-content: center; }

  .contacts { position: absolute; left: 46px; top: 244px; font-family: "Lato", sans-serif; font-size: 23px; color: var(--ink); }
  .contact-row { display: flex; align-items: flex-start; gap: 16px; margin-bottom: 18px; }
  .contact-row .lines { line-height: 32px; }
  .contact-icon { width: 38px; height: 38px; flex: none; margin-top: -2px; }

  .holder { position: absolute; left: 615px; width: 400px; top: 238px; text-align: center; color: var(--paper); }
  .holder-name { font-family: "Libre Baskerville", serif; font-weight: 700; font-variant: small-caps; font-size: 31px; letter-spacing: 0.5px; }
  .holder-title { font-family: "Lato", sans-serif; font-size: 24px; margin-top: 10px; }

  .services { position: absolute; left: 0; right: 0; top: 282px; text-align: center; font-family: "Lato", sans-serif; }
  .services-heading { font-weight: 700; font-size: 28px; color: var(--ink); margin-bottom: 10px; }
  .services-list { font-size: 23px; line-height: 32px; color: var(--service-red); }
</style>
</head>
<body>
<div class="sheet">

  <!-- Front -->
  <div class="card-frame front">
    <div class="card">
      <svg class="card-shapes" viewBox="0 0 1015 580" aria-hidden="true">
        <polygon fill="var(--charcoal)" points="660,0 1015,0 1015,580 600,580"/>
        <polygon fill="var(--red)" points="622,0 660,0 600,580 562,580"/>
        <polygon fill="var(--red-dark)" points="598,0 610,0 550,580 538,580"/>
        <rect fill="var(--red)" x="0" y="552" width="500" height="28"/>
        <rect fill="var(--red-dark)" x="0" y="538" width="360" height="8"/>
      </svg>

      <div class="brand"><span class="brand-dot"></span>VELMORA BUILDWORKS</div>

      <div class="contacts">
        <div class="contact-row">
          <svg class="contact-icon" viewBox="0 0 38 38" aria-hidden="true">
            <circle cx="19" cy="19" r="18" fill="var(--charcoal)"/>
            <path d="M12 11c1-1 2.5-1 3 0l2 3c.5 1 0 2-1 2.5 1 2.5 2.5 4 5 5 .5-1 1.5-1.5 2.5-1l3 2c1 .5 1 2 0 3-2 2-5 2-9-1.5S10 13 12 11z" fill="var(--paper)"/>
          </svg>
          <div class="lines">+65 81550427 (Singapore)<br>+974 66208314 (Qatar)</div>
        </div>
        <div class="contact-row">
          <svg class="contact-icon" viewBox="0 0 38 38" aria-hidden="true">
            <circle cx="19" cy="19" r="18" fill="var(--charcoal)"/>
            <rect x="10" y="12.5" width="18" height="13" fill="none" stroke="var(--paper)" stroke-width="1.8"/>
            <path d="M10 12.5l9 7 9-7" fill="none" stroke="var(--paper)" stroke-width="1.8"/>
          </svg>
          <div class="lines">info@velmora-buildworks.example</div>
        </div>
        <div class="contact-row">
          <svg class="contact-icon" viewBox="0 0 38 38" aria-hidden="true">
            <circle cx="19" cy="19" r="18" fill="var(--charcoal)"/>
            <circle cx="19" cy="19" r="9" fill="none" stroke="var(--paper)" stroke-width="1.8"/>
            <ellipse cx="19" cy="19" rx="4" ry="9" fill="none" stroke="var(--paper)" stroke-width="1.5"/>
            <line x1="10" y1="19" x2="28" y2="19" stroke="var(--paper)" stroke-width="1.5"/>
          </svg>
          <div class="lines">www.velmora-buildworks.example</div>
        </div>
      </div>

      <div class="holder">
        <div class="holder-name">Card Holder Name</div>
        <div class="holder-title">Job Title Here</div>
      </div>
    </div>
  </div>

  <!-- Back -->
  <div class="card-frame back">
    <div class="card">
      <svg class="card-shapes" viewBox="0 0 1015 580">
        <defs>
          <linearGradient id="globe-tone" x1="0" y1="0" x2="0" y2="1">
            <stop offset="0" stop-color="#f3f3f3"/>
            <stop offset="1" stop-color="#dcdcdc"/>
          </linearGradient>
        </defs>
        <g role="img" aria-label="Faint grey world map wrapping a globe, showing worldwide service">
          <path d="M0 250 C120 90 320 0 507 0 C700 0 900 90 1015 250 L1015 270 C900 240 700 440 507 440 C320 440 110 260 0 270 Z" fill="url(#globe-tone)" opacity="0.85"/>
        </g>
        <rect fill="var(--red-dark)" x="0" y="530" width="1015" height="8"/>
        <rect fill="var(--red)" x="0" y="544" width="1015" height="36"/>
      </svg>

      <div class="brand"><span class="brand-dot"></span>VELMORA BUILDWORKS</div>

      <div class="services">
        <div class="services-heading">Our Services</div>
        <div class="services-list">
          Exhibition Booth Fabrication | Outdoor Booth Setup | Interior Design | Installation and Dismantle<br>
          Exhibition Management | Shell Scheme Display Booth | Custom Stand Design<br>
          Exhibition Furniture and Equipment | Exhibition Project Management
        </div>
      </div>
    </div>
  </div>

</div>
</body>
</html>
```